Design a newsletter for a crypto gateway payment company

The project is about making the design for a newsletter (sent by email) for a crypto payment gateway. The design should include all usual and necessary parts found in a newsletter (header, one main article with illustration and link to the full content, some secondary articles with or without illustration and link to the company blog, footer with links to unsubscribe page and various information about the company, section separator, secondary articles ...).
The design may re-use some elements from the company web site https://quorvelpay.io, but feel free to innovate.
The design should be responsive and be as good in all email clients and all sizes of display from handset to desktop with everything in between.
I've added a few screenshot of the previous newsletter as they were sent to users.
Good luck and be an artist. No AI stuff, please.

```html
<!DOCTYPE html>
<html lang="en">
<head>
<meta charset="utf-8">
<title>The Quorvel Times – March 2024</title>
<link rel="stylesheet" href="https://fonts.googleapis.com/css2?family=Roboto:wght@400;500;700&display=swap">
<style>
  :root {
    --navy: #16184a;
    --ink: #1f2a4d;
    --body: #555a66;
    --muted: #333;
    --gold: #f5c518;
    --orange: #fdab12;
    --mist: #f2f7fc;
    --footer: #d8e6f2;
    --white: #ffffff;
  }
  * { box-sizing: border-box; margin: 0; padding: 0; }
  html, body { width: 1158px; height: 1200px; overflow: hidden; background: var(--white); }
  body { font-family: "Roboto", Arial, sans-serif; color: var(--ink); position: relative; }

  .masthead { position: absolute; left: 0; top: 0; width: 1158px; height: 146px; background: var(--navy); }
  .masthead__brand { position: absolute; left: 97px; top: 50px; font-size: 38px; font-weight: 500; color: var(--white); letter-spacing: -0.3px; }
  .masthead__date { position: absolute; left: 998px; top: 58px; font-size: 20px; color: var(--gold); }

  .hero { position: absolute; left: 0; top: 146px; width: 1158px; height: 459px; overflow: hidden; background: var(--white); }
  .hero__backdrop { position: absolute; left: 0; top: 0; }
  .hero__title { position: absolute; left: 91px; top: 46px; width: 520px; font-size: 35px; line-height: 46px; font-weight: 500; color: var(--ink); }
  .hero__lead { position: absolute; left: 91px; top: 146px; width: 480px; font-size: 15px; line-height: 25px; color: var(--body); }
  .hero__points { position: absolute; left: 91px; top: 240px; list-style: none; }
  .hero__points li { position: relative; padding-left: 22px; height: 35px; font-size: 15px; line-height: 22px; color: var(--body); }
  .hero__points li::before { content: ""; position: absolute; left: 0; top: 6px; width: 12px; height: 12px; border-radius: 50%; background: var(--gold); }
  .hero__button { position: absolute; left: 90px; top: 363px; width: 123px; height: 45px; background: linear-gradient(90deg, var(--orange), var(--gold)); box-shadow: 0 6px 14px rgba(253,171,18,.3); color: var(--white); font-size: 11px; font-weight: 700; line-height: 45px; text-align: center; text-decoration: none; letter-spacing: .3px; }
  .hero__media { position: absolute; left: 607px; top: 53px; width: 486px; height: 330px; background: linear-gradient(160deg, #e9c46a 0%, #a37a3a 35%, #4a4038 70%, #2a2a2e 100%); }

  .story { position: absolute; width: 460px; height: 145px; }
  .story__title { position: absolute; left: 0; top: 6px; font-size: 17.5px; line-height: 21px; font-weight: 500; color: var(--ink); }
  .story__text { position: absolute; left: 0; top: 53px; width: 220px; font-size: 7px; line-height: 11px; color: var(--muted); }
  .story__link { position: absolute; left: 1px; font-size: 11px; color: #111; text-decoration: underline; }
  .story__media { position: absolute; left: 241px; top: 0; width: 209px; height: 145px; }
  .story--a { left: 90px; top: 664px; }
  .story--b { left: 629px; top: 664px; }
  .story--c { left: 90px; top: 856px; }
  .story--d { left: 629px; top: 856px; }
  .story--b .story__media, .story--d .story__media { left: 233px; }
  .media--desk { background: linear-gradient(135deg, #2b2b33, #6d6f78 55%, #c9c9cf); }
  .media--chart { background: linear-gradient(180deg, #0d2a6b, #0a1a4a 60%, #1a3a7a); }
  .media--bank { background: linear-gradient(135deg, #cfe0f5, #5a86c8 55%, #223e80); }
  .media--coin { background: linear-gradient(135deg, #0a2a8a, #123ab8 50%, #0a1650); }

  .preferences { position: absolute; left: 0; top: 1066px; width: 1158px; text-align: center; font-size: 14px; color: #111; }
  .preferences a { color: #111; text-decoration: underline; }
  .preferences span { margin: 0 14px; }

  .footer { position: absolute; left: 0; top: 1105px; width: 1158px; height: 95px; background: var(--footer); font-size: 14px; color: #111; }
  .footer__legal { position: absolute; left: 86px; top: 35px; }
  .footer__links { position: absolute; right: 82px; top: 35px; }
  .footer__links a { color: #111; text-decoration: none; }
  .footer__links span { margin: 0 14px; }
</style>
</head>
<body>
  <header class="masthead">
    <div class="masthead__brand">The Quorvel Times</div>
    <div class="masthead__date">March 2024</div>
  </header>

  <section class="hero">
    <svg class="hero__backdrop" width="1158" height="459" aria-hidden="true">
      <path d="M0 60 C120 40 240 90 290 200 C330 300 300 400 340 459 L0 459 Z" fill="#f5f9fd"/>
      <path d="M260 459 C420 420 700 440 1158 420 L1158 459 Z" fill="#f7fafd"/>
      <circle cx="600" cy="200" r="7" fill="#eef3f9"/>
    </svg>
    <h1 class="hero__title">We Are Leading International Digital Currency Agency</h1>
    <p class="hero__lead">This should be used to tell a story and let your users know a little more about your product or service. How can you benefit them? convince them to use your service.</p>
    <ul class="hero__points">
      <li>We Are Passionate And Creative</li>
      <li>Open Source And Free Software</li>
      <li>Very Fast And Reliable</li>
    </ul>
    <a class="hero__button" href="https://quorvelpay.io">LEARN MORE</a>
    <div class="hero__media" role="img" aria-label="Hand holding a smartphone above a pile of gold and silver crypto coins on a laptop"></div>
  </section>

  <article class="story story--a">
    <h2 class="story__title">Invest In Cryptocoin<br>Easy Way To Trade Bitcoin.</h2>
    <p class="story__text">Launch your campaign and benefit from our expertise on designing and managing conversion centered landing pages.</p>
    <a class="story__link" style="top:99px" href="https://quorvelpay.io">LEARN MORE</a>
    <div class="story__media media--desk" role="img" aria-label="Person signing a financial report at a desk"></div>
  </article>

  <article class="story story--b">
    <h2 class="story__title">Banking Platform That<br>Enables Currency Solutions.</h2>
    <p class="story__text">This should be used to tell a story and let your users know a little more about your product or service. How can you benefit them? convince them to use your service.</p>
    <a class="story__link" style="top:107px" href="https://quorvelpay.io">LEARN MORE</a>
    <div class="story__media media--chart" role="img" aria-label="Trading chart with candlesticks on a dark blue screen"></div>
  </article>

  <article class="story story--c">
    <h2 class="story__title" style="top:31px">Banking Platform That<br>Enables Currency Solutions.</h2>
    <p class="story__text" style="top:78px">This should be used to tell a story and let your users know a little more about your product or service. How can you benefit them? convince them to use your service.</p>
    <a class="story__link" style="top:132px" href="https://quorvelpay.io">LEARN MORE</a>
    <div class="story__media media--bank" role="img" aria-label="Hands using online banking on a digital screen"></div>
  </article>

  <article class="story story--d">
    <h2 class="story__title" style="top:13px">Invest In Cryptocoin<br>Easy Way To Trade Bitcoin.</h2>
    <p class="story__text" style="top:60px">Launch your campaign and benefit from our expertise on designing and managing conversion centered landing pages.</p>
    <a class="story__link" style="top:105px" href="https://quorvelpay.io">LEARN MORE</a>
    <div class="story__media media--coin" role="img" aria-label="Glowing digital currency symbol over a blue data background"></div>
  </article>

  <nav class="preferences">
    <a href="https://quorvelpay.io">Unsubscribe</a><span>|</span><a href="https://quorvelpay.io">Manage Preferences</a>
  </nav>

  <footer class="footer">
    <div class="footer__legal">© Quorvel Technologies Pte. Ltd.2024 | All Rights Reserved</div>
    <div class="footer__links">
      <a href="https://quorvelpay.io">About Us</a><span>|</span><a href="https://quorvelpay.io">Contact Us</a><span>|</span><a href="https://quorvelpay.io">Privacy Policy</a>
    </div>
  </footer>
</body>
</html>
```